Patient Fact sheets for medical conditions and treatments

Hi,

I need a new design for my patient fact sheets. I am moving from my current clinic and I am looking from a new look.

I have attached
1. a current Fact sheet
2. New home page to the website
3. New Logo.

They need to be single page and easily readable for patients.

The will be in both PDF and print form in the future.

Target Market(s)

Patients with chronic pain age 40+

Font styles to use
Serif

Requirements
Must have
• My logo, should be inline with design elements on the Front page provided.

Please use the same font as the Logo

```html
<!DOCTYPE html>
<html lang="en">
<head>
<meta charset="utf-8">
<title>Fact Sheet – Platelet Rich Plasma (PRP) Therapy</title>
<link href="https://fonts.googleapis.com/css2?family=Cinzel:wght@400;500&family=Montserrat:wght@600;700&family=Open+Sans:wght@400;600&display=swap" rel="stylesheet">
<style>
:root{
  --teal:#139ba8;
  --teal-dark:#0f8794;
  --slate:#5f666e;
  --slate-dark:#50565d;
  --orange:#f4a31a;
  --ink:#3d4247;
  --paper:#ffffff;
  --panel:#f1f1f2;
}
*{box-sizing:border-box;margin:0;padding:0}
html,body{width:900px;height:1200px;overflow:hidden;background:var(--paper)}
body{position:relative;font-family:"Open Sans",Arial,sans-serif;color:var(--ink)}
.sheet{position:absolute;inset:0;overflow:hidden}

/* header */
.header-band{position:absolute;left:0;top:0;width:900px;height:146px;background:var(--slate)}
.brand{position:absolute;left:34px;top:48px;display:flex;align-items:center;gap:12px;
  font-family:"Cinzel",Georgia,serif;font-weight:400;color:#fff;font-size:26px;letter-spacing:1px;line-height:1.1}
.brand-mark{width:14px;height:14px;background:#fff}
.factsheet-tab{position:absolute;left:0;top:0;width:900px;height:170px}
.factsheet-title{position:absolute;right:40px;top:42px;font-family:"Cinzel",Georgia,serif;font-weight:500;
  font-size:62px;color:#fff;letter-spacing:1px}

.main-title{position:absolute;left:34px;top:180px;font-family:"Cinzel",Georgia,serif;font-weight:500;
  font-size:40px;color:var(--teal);letter-spacing:.5px;white-space:nowrap}

/* tabs */
.tab{position:absolute;background:var(--orange);color:#fff;font-family:"Montserrat",Arial,sans-serif;
  font-weight:700;font-size:22px;letter-spacing:1px;display:flex;align-items:center;justify-content:center}
.tab-what{left:0;top:245px;width:276px;height:42px;border-radius:0 21px 21px 0}
.tab-how{left:236px;top:478px;width:400px;height:46px;border-radius:6px;z-index:2}

.intro{position:absolute;left:36px;top:304px;width:325px;font-size:10.5px;line-height:1.45}
.intro p{margin-bottom:11px}

.photo{position:absolute;left:385px;top:243px;width:475px;height:214px;border:2px solid #8a8f95;
  background:linear-gradient(110deg,#d8dcdf 0%,#eef0f1 35%,#f3d35a 52%,#f0c53a 58%,#e6e8ea 70%,#cfd3d6 100%)}

/* how band */
.how-band{position:absolute;left:0;top:493px;width:900px;height:194px;background:var(--slate);color:#fff;
  padding:46px 36px 0;font-size:9.5px;line-height:1.4}
.how-band p{margin-bottom:10px}
.how-band p:last-child{margin-bottom:0}

/* columns */
.col-left{position:absolute;left:36px;top:712px;width:390px}
.col-right{position:absolute;left:506px;top:712px;width:356px}
.divider{position:absolute;left:470px;top:715px;width:1px;height:250px;background:#c9ccce}
.section-head{font-family:"Montserrat",Arial,sans-serif;font-weight:600;color:var(--teal);font-size:16px;
  letter-spacing:.5px;margin-bottom:10px}
.lead{font-family:"Montserrat",Arial,sans-serif;font-weight:600;color:var(--orange);font-size:11px;line-height:1.4;margin-bottom:8px}
.ticks{list-style:none;font-size:10.5px;line-height:1.35}
.ticks li{display:flex;gap:12px;margin-bottom:12px}
.ticks svg{flex:none;width:11px;height:11px;margin-top:2px}
.results p{font-size:10.5px;line-height:1.45}
.results .section-head{margin-top:4px}
.treat-grid{list-style:none;display:grid;grid-template-columns:1.2fr 1fr 1fr;column-gap:8px;row-gap:10px;font-size:10px;line-height:1.25}
.treat-grid li{display:flex;gap:7px}
.treat-grid svg{flex:none;width:10px;height:10px;margin-top:1px}
.ask{margin-top:34px;font-weight:600;font-size:13.5px;line-height:1.4;color:var(--ink)}

.disclaimer{position:absolute;left:506px;top:943px;width:354px;height:170px;background:var(--panel);
  border-radius:10px;padding:18px 22px}
.disclaimer h3{font-family:"Montserrat",Arial,sans-serif;font-weight:600;color:var(--teal);font-size:15px;margin-bottom:10px}
.disclaimer p{font-size:8px;line-height:1.45}

/* footer */
.footer{position:absolute;left:0;top:1118px;width:900px;height:82px}
.footer-text{position:absolute;color:#fff;font-family:"Montserrat",Arial,sans-serif;font-weight:600;font-size:11px;line-height:1.45}
.footer-text svg{width:12px;height:12px;margin-right:10px;vertical-align:-2px}
.address{left:36px;top:14px;display:flex;gap:10px}
.address svg{margin-top:2px}
.phones{left:298px;top:14px}
.webs{left:510px;top:14px}
.follow{left:780px;top:14px;text-align:center}
.social{display:flex;gap:8px;justify-content:center;margin-top:6px}
.social span{width:14px;height:14px;background:#fff;display:block}
.vsep{position:absolute;top:20px;width:1px;height:42px;background:rgba(255,255,255,.7)}
</style>
</head>
<body>
<div class="sheet">

  <div class="header-band"></div>
  <svg class="factsheet-tab" viewBox="0 0 900 170" aria-hidden="true">
    <polygon points="440,20 900,20 900,166 365,166" fill="var(--teal)"/>
  </svg>
  <div class="brand"><span class="brand-mark"></span><span>DR ALAN MORROW</span></div>
  <div class="factsheet-title">FACT SHEET</div>

  <h1 class="main-title">PLATELET RICH PLASMA (PRP) THERAPY</h1>

  <div class="tab tab-what">WHAT IS PRP?</div>
  <div class="intro">
    <p>Platelet-Rich Plasma (PRP) is concentrated platelets and white blood cells derived from your own blood.</p>
    <p>Platelet Rich Plasma Injection Therapy (PRP therapy), is a growing treatment approach for soft tissue injuries including tendon, muscle and ligaments. It is also showing good results for mild to moderate osteoarthritis.</p>
    <p>While this approach has been used overseas for many years, it's fairly new to Australia in the treatment of musculoskeletal and orthopaedic conditions.</p>
  </div>
  <div class="photo" role="img" aria-label="Photo of a gloved hand holding two test tubes of separated yellow plasma"></div>

  <div class="tab tab-how">HOW DOES PRP WORK?</div>
  <section class="how-band">
    <p>Some tissues in the body have a poor blood supply or respond poorly to excessive load, ultimately failing to heal naturally. While some of our primary treatment such as physiotherapy, massage, biomechanical correction and other forms of treatment are used to treat these soft tissue injuries, sometimes the body fails to respond.</p>
    <p>PRP therapy utilises the healing properties in blood to allow a healing reaction to occur in a tissue that's not healing on its own. Our blood has small granules called 'platelets', which contain special growth factors that when released, allow stem cells in the particular tissue to 'switch' on and cause new tissue to be created and heal the injured area.</p>
    <p>Take the example of achilles tendinopathy. If the achilles is painful, thickened and not responding to rehabilitation, then the sports physician will inject the PRP into the achilles which will cause the tendon cells (tenocytes/fibroblasts) to create new achilles collagen to strengthen the achilles. White blood cells also enter the area to mop up any achilles tissue that may have been damaged due to the ongoing pain and thickening in the area.</p>
  </section>

  <div class="col-left">
    <h2 class="section-head">Role of platelets &amp; growth factors</h2>
    <p class="lead">PRP contains highly concentrated platelets. Platelets have been identified to secrete growth factors, which are known to play a role in:</p>
    <ul class="ticks">
      <li><svg viewBox="0 0 12 12"><rect x=".6" y="1.6" width="9.5" height="9.5" fill="none" stroke="var(--teal)" stroke-width="1.2"/><path d="M3 6l2.3 2.5L11 1.5" fill="none" stroke="var(--teal)" stroke-width="1.4"/></svg>Increasing tissue vascularity and increasing the rate of epithelial tissue production (wound healing)</li>
      <li><svg viewBox="0 0 12 12"><rect x=".6" y="1.6" width="9.5" height="9.5" fill="none" stroke="var(--teal)" stroke-width="1.2"/><path d="M3 6l2.3 2.5L11 1.5" fill="none" stroke="var(--teal)" stroke-width="1.4"/></svg>Attracting other cells that fight infection</li>
      <li><svg viewBox="0 0 12 12"><rect x=".6" y="1.6" width="9.5" height="9.5" fill="none" stroke="var(--teal)" stroke-width="1.2"/><path d="M3 6l2.3 2.5L11 1.5" fill="none" stroke="var(--teal)" stroke-width="1.4"/></svg>Acting as a seal during closures</li>
      <li><svg viewBox="0 0 12 12"><rect x=".6" y="1.6" width="9.5" height="9.5" fill="none" stroke="var(--teal)" stroke-width="1.2"/><path d="M3 6l2.3 2.5L11 1.5" fill="none" stroke="var(--teal)" stroke-width="1.4"/></svg>Providing an immediate surgical hemostatic agent (reduction of bleeding)</li>
      <li><svg viewBox="0 0 12 12"><rect x=".6" y="1.6" width="9.5" height="9.5" fill="none" stroke="var(--teal)" stroke-width="1.2"/><path d="M3 6l2.3 2.5L11 1.5" fill="none" stroke="var(--teal)" stroke-width="1.4"/></svg>Osteogenesis (bone regeneration and repair).</li>
    </ul>
    <div class="results">
      <h2 class="section-head">What are the expected results of prp?</h2>
      <p>Because the goal of PRP therapy is to resolve pain through healing, it could prove to have lasting results. Initial improvement may be seen within a few weeks, gradually increasing as the healing progresses. Research studies and clinical practice have shown PRP therapy to be very effective at relieving pain and returning patients to their normal lives. The need for surgery can also be greatly reduced by treating injured tissues before the damage progresses and the condition is irreversible.</p>
    </div>
  </div>

  <div class="divider"></div>

  <div class="col-right">
    <h2 class="section-head">What can prp treat?</h2>
    <p class="lead">PRP therapy can be used for:</p>
    <ul class="treat-grid">
      <li><svg viewBox="0 0 12 12"><rect x=".6" y="1.6" width="9.5" height="9.5" fill="none" stroke="var(--teal)" stroke-width="1.2"/><path d="M3 6l2.3 2.5L11 1.5" fill="none" stroke="var(--teal)" stroke-width="1.4"/></svg>Orthopedic surgery</li>
      <li><svg viewBox="0 0 12 12"><rect x=".6" y="1.6" width="9.5" height="9.5" fill="none" stroke="var(--teal)" stroke-width="1.2"/><path d="M3 6l2.3 2.5L11 1.5" fill="none" stroke="var(--teal)" stroke-width="1.4"/></svg>neurosurgery</li>
      <li><svg viewBox="0 0 12 12"><rect x=".6" y="1.6" width="9.5" height="9.5" fill="none" stroke="var(--teal)" stroke-width="1.2"/><path d="M3 6l2.3 2.5L11 1.5" fill="none" stroke="var(--teal)" stroke-width="1.4"/></svg>neurosurgery</li>
      <li><svg viewBox="0 0 12 12"><rect x=".6" y="1.6" width="9.5" height="9.5" fill="none" stroke="var(--teal)" stroke-width="1.2"/><path d="M3 6l2.3 2.5L11 1.5" fill="none" stroke="var(--teal)" stroke-width="1.4"/></svg>Cardiac surgery</li>
      <li><svg viewBox="0 0 12 12"><rect x=".6" y="1.6" width="9.5" height="9.5" fill="none" stroke="var(--teal)" stroke-width="1.2"/><path d="M3 6l2.3 2.5L11 1.5" fill="none" stroke="var(--teal)" stroke-width="1.4"/></svg>vascular surgery</li>
      <li><svg viewBox="0 0 12 12"><rect x=".6" y="1.6" width="9.5" height="9.5" fill="none" stroke="var(--teal)" stroke-width="1.2"/><path d="M3 6l2.3 2.5L11 1.5" fill="none" stroke="var(--teal)" stroke-width="1.4"/></svg>vascular surgery</li>
      <li><svg viewBox="0 0 12 12"><rect x=".6" y="1.6" width="9.5" height="9.5" fill="none" stroke="var(--teal)" stroke-width="1.2"/><path d="M3 6l2.3 2.5L11 1.5" fill="none" stroke="var(--teal)" stroke-width="1.4"/></svg>Plastic and cosmetic surgery</li>
      <li><svg viewBox="0 0 12 12"><rect x=".6" y="1.6" width="9.5" height="9.5" fill="none" stroke="var(--teal)" stroke-width="1.2"/><path d="M3 6l2.3 2.5L11 1.5" fill="none" stroke="var(--teal)" stroke-width="1.4"/></svg>Oral maxillofacial</li>
      <li><svg viewBox="0 0 12 12"><rect x=".6" y="1.6" width="9.5" height="9.5" fill="none" stroke="var(--teal)" stroke-width="1.2"/><path d="M3 6l2.3 2.5L11 1.5" fill="none" stroke="var(--teal)" stroke-width="1.4"/></svg>Ear, nose, throat (ENT) surgery</li>
    </ul>
    <p class="ask">Ask your doctor whether plateletrich plasma is appropriate for your surgical procedure.</p>
  </div>

  <aside class="disclaimer">
    <h3>Disclaimer</h3>
    <p>Please note the information in this patient fact sheet is general in nature and does not replace advice from your own doctor or other health professional. At our clinic, every patient is assessed on an individual basis. We aim to offer careful, modern and evidence-based care planned around each person. Because of this, suggested treatments and their results will differ from one patient to another. To learn whether a treatment suits your condition, please ask one of our doctors during your next visit.</p>
  </aside>

  <footer class="footer">
    <svg width="900" height="82" viewBox="0 0 900 82" style="position:absolute;left:0;top:0" aria-hidden="true">
      <rect x="0" y="0" width="900" height="82" fill="var(--slate)"/>
      <polygon points="0,0 440,0 490,82 0,82" fill="var(--teal)"/>
      <rect x="0" y="0" width="900" height="3" fill="var(--teal)"/>
    </svg>
    <div class="footer-text address">
      <svg viewBox="0 0 12 12"><path d="M6 .5a4 4 0 0 0-4 4c0 3 4 7 4 7s4-4 4-7a4 4 0 0 0-4-4zm0 5.6a1.6 1.6 0 1 1 0-3.2 1.6 1.6 0 0 1 0 3.2z" fill="#fff"/></svg>
      <span>Harbour Pain Clinic Bayview House,<br>Level 2 48 Harbour Street<br>Seaford VIC 3999</span>
    </div>
    <div class="footer-text phones">
      <div><svg viewBox="0 0 12 12"><path d="M2.5 1l2 2.2-1 1.3a7 7 0 0 0 4 4l1.3-1 2.2 2-1.4 1.8C5 11 1 7 .8 2.4z" fill="#fff"/></svg>03 9000 4120</div>
      <div style="margin-top:6px"><svg viewBox="0 0 12 12"><rect x="3" y="1" width="6" height="3" fill="#fff"/><rect x="1" y="4.5" width="10" height="5" rx="1" fill="#fff"/><rect x="3" y="8" width="6" height="3" fill="#fff"/></svg>03 9000 4121</div>
    </div>
    <div class="footer-text webs">
      <div><svg viewBox="0 0 12 12"><rect x="1" y="2.5" width="10" height="7" fill="#fff"/><path d="M1 2.5l5 4 5-4" fill="none" stroke="var(--slate)" stroke-width="1"/></svg>info@harbourpainclinic.example</div>
      <div style="margin-top:6px"><svg viewBox="0 0 12 12"><circle cx="6" cy="6" r="5" fill="none" stroke="#fff" stroke-width="1.2"/><ellipse cx="6" cy="6" rx="2" ry="5" fill="none" stroke="#fff" stroke-width="1"/><path d="M1 6h10" stroke="#fff" stroke-width="1"/></svg>www.harbourpainclinic.example</div>
    </div>
    <div class="vsep" style="left:752px"></div>
    <div class="footer-text follow">
      <div>Follow Us</div>
      <div class="social"><span></span><span></span><span></span></div>
    </div>
  </footer>

</div>
</body>
</html>
```